Website for a Party Bus charter business

Please prepare a site for a local party bus charter company names Holloway Bus Company.
They hire a party bus, chatrer bus, boat hire and party trailer hire (place holder photos fine for these items).
I have included a wireframe design. This should be used, however creative licence is fully extended
Delivery of PSD is required and all fonts and source files
The client likes: http://www.tallquorin.com.au/ but must not look completely the same.
Should use a gold (simualr to #D1CFA1) colour, even if just background.
Updates
Hi All, just wondering if anyone is working on this as I have not received any responses or questions?
Is there anything I can do to assist?
Thanks all for the great submissions. I will be sending these onto the client today. Will let you know the outcome as soon as I can
Industry/Entity Type
Business
Look and feel
Each slider illustrates characteristics of the customer's brand and the style your logo design should communicate.

```html
<!DOCTYPE html>
<html lang="en">
<head>
<meta charset="utf-8">
<title>Holloway Bus Company</title>
<link href="https://fonts.googleapis.com/css2?family=Oswald:wght@500&family=Open+Sans:wght@400;600&family=Arimo:wght@400;700&display=swap" rel="stylesheet">
<style>
:root{
  --bg-deep:#17172a;
  --bg-mid:#26263f;
  --text-light:#ffffff;
  --text-muted:#a9a9bd;
  --gold-top:#f3dc78;
  --gold-bottom:#d7ac2a;
  --gold-line:#9a7a1c;
  --ink:#111111;
  --link-red:#e0241b;
  --card:#ffffff;
  --rule:#4a4a66;
  --social-red:#d3252f;
  --social-sky:#28a9e0;
  --social-blue:#3b5a9a;
}
*{margin:0;padding:0;box-sizing:border-box}
html,body{width:797px;height:1200px;overflow:hidden}
body{
  position:relative;
  background:radial-gradient(ellipse at 50% 40%,var(--bg-mid) 0%,var(--bg-deep) 75%);
  font-family:Arimo,Arial,sans-serif;color:var(--text-light);
}
.abs{position:absolute}
.brand{left:140px;top:18px;width:130px;text-align:center}
.brand-mark{width:58px;height:58px;border-radius:50%;background:#6c6fb8;margin:0 auto 4px}
.brand-name{font-family:Arimo,Arial,sans-serif;font-weight:700;color:var(--text-light);font-size:19px;line-height:20px}
.brand-name small{display:block;font-size:13px;letter-spacing:3px;font-weight:700}
.connect{right:118px;top:10px;font-size:8px;color:#d8d8e6;display:flex;align-items:center;gap:6px}
.social{display:flex;gap:4px}
.social span{width:10px;height:10px;display:block;border-radius:2px}
.s1{background:var(--social-red)}.s2{background:var(--social-sky)}.s3{background:var(--social-blue)}
.phone{right:117px;top:25px;font-family:"Open Sans",sans-serif;font-size:19px;color:var(--text-light)}
.like-box{left:490px;top:57px;width:38px;height:11px;display:flex;gap:2px}
.like-box span{background:var(--social-blue);width:24px;border-radius:2px}
.like-box em{background:#fff;width:11px;border-radius:1px}
.search{left:537px;top:54px;width:144px;height:17px;display:flex}
.search input{flex:1;border:0;font-size:8px;padding-left:7px;font-family:Arimo,Arial,sans-serif;color:#555}
.search button{width:20px;border:0;background:#3c5ab0;display:flex;align-items:center;justify-content:center}
.nav{left:294px;top:80px;width:387px;height:26px;background:linear-gradient(var(--gold-top),var(--gold-bottom));
  display:flex;align-items:center;justify-content:space-around;font-family:"Open Sans",sans-serif;font-size:9px;color:var(--ink);
  border-bottom:1px solid var(--gold-line)}
.nav i{font-style:normal;color:#6b5410}
.hero{left:121px;top:116px;width:560px;height:244px;border:4px solid #fff;
  background:linear-gradient(100deg,#1b2050 0%,#3a3f8a 30%,#6a4a7e 55%,#b07a64 75%,#3a2a3a 100%)}
.hero-title{left:38px;top:128px;font-family:Oswald,sans-serif;font-weight:500;font-size:31px;line-height:34px}
.hero-sub{left:38px;top:164px;font-family:"Open Sans",sans-serif;font-size:28px}
.dots{right:60px;bottom:6px;display:flex;gap:3px}
.dots span{width:7px;height:7px;border-radius:50%;background:#fff}
h2{font-family:Arimo,Arial,sans-serif;font-weight:400;font-size:20px;color:var(--text-light)}
.copy{font-size:8.4px;line-height:12.5px;color:var(--text-muted)}
.welcome-title{left:121px;top:379px}
.welcome-copy{left:121px;top:414px;width:366px}
.fb-box{left:510px;top:385px;width:170px;height:100px;background:#fff;padding:6px;color:#333;font-size:6px}
.fb-box .row{display:flex;gap:4px;align-items:center}
.fb-box .mark{width:16px;height:16px;border-radius:50%;background:#6c6fb8}
.fb-box .name{color:var(--social-blue);font-size:6.5px}
.fb-box .btn{width:24px;height:9px;background:var(--social-blue);border-radius:2px;margin:3px 0 0 29px}
.fb-box hr{border:0;border-top:1px solid #ddd;margin:5px 0}
.fb-box .faces{display:flex;gap:4px;margin-top:4px}
.fb-box .faces span{width:22px;height:22px;background:linear-gradient(#c08a70,#5a3a3a)}
.fb-box .foot{margin-top:6px;color:#999;font-size:5px}
.gold-btn{background:linear-gradient(var(--gold-top),var(--gold-bottom));color:var(--ink);font-family:Arimo,Arial,sans-serif;
  border:1px solid var(--gold-line);display:flex;align-items:center;justify-content:center}
.services-title{left:121px;top:492px}
.view-all{left:616px;top:501px;width:63px;height:17px;font-size:12px}
.card{width:267px;height:92px;background:var(--card);color:var(--ink)}
.card .thumb{position:absolute;left:14px;top:13px;width:107px;height:66px}
.card h3{position:absolute;left:132px;top:13px;font-family:"Open Sans",sans-serif;font-weight:400;font-size:12px}
.card p{position:absolute;left:132px;top:33px;width:122px;font-size:7.3px;line-height:11px}
.card p b{font-weight:400;color:var(--link-red)}
.coast-title{left:121px;top:750px}
.coast-photo{left:121px;top:787px;width:277px;height:140px;border:4px solid #fff;background:linear-gradient(160deg,#5d8fc9,#2c6fb0 40%,#b08070 70%,#2d3a55)}
.coast-copy{left:409px;top:789px;width:270px}
.book{left:564px;top:893px;width:113px;height:28px;font-size:17px}
.rule{left:121px;width:558px;border-top:1px solid var(--rule)}
.foot-title{top:961px;font-size:15px}
.quote-copy{left:121px;top:990px;width:180px}
.get-quote{left:121px;top:1051px;width:114px;height:28px;font-size:17px}
.blog{left:337px;width:170px;height:45px}
.blog .thumb{position:absolute;left:0;top:0;width:51px;height:44px;background:linear-gradient(#d8b8a0,#3a3a5a)}
.blog h4{position:absolute;left:58px;top:1px;font-size:8px;font-weight:700}
.blog p{position:absolute;left:58px;top:12px;width:112px;font-size:7.2px;line-height:11px;color:var(--text-muted)}
.vip-copy{left:542px;top:990px;width:140px}
.field{left:542px;width:139px;height:16px;background:#fff;color:#222;font-size:8px;padding:4px 0 0 8px}
.join{left:542px;top:1077px;width:63px;height:17px;font-size:11px}
.copyright{left:121px;top:1125px;font-size:7px;color:var(--text-muted);line-height:12px}
.copyright a{color:var(--text-muted)}
.foot-social{right:118px;top:1132px}
</style>
</head>
<body>
<header>
  <div class="abs brand">
    <div class="brand-mark"></div>
    <div class="brand-name">Holloway Bus<small>COMPANY</small></div>
  </div>
  <div class="abs connect">
    <svg width="11" height="10" viewBox="0 0 11 10"><path d="M5.5 0L0 5h1.5v5h3V7h2v3h3V5H11z" fill="#fff"/></svg>
    Connect with us!
    <div class="social"><span class="s1"></span><span class="s2"></span><span class="s3"></span></div>
  </div>
  <div class="abs phone">123 456 7890</div>
  <div class="abs like-box"><span></span><em></em></div>
  <form class="abs search">
    <input type="text" placeholder="Enter Keyword here">
    <button type="button" aria-label="Search"><svg width="10" height="10" viewBox="0 0 10 10"><circle cx="4" cy="4" r="3" stroke="#fff" stroke-width="1.5" fill="none"/><path d="M6.2 6.2L9.3 9.3" stroke="#fff" stroke-width="1.6"/></svg></button>
  </form>
  <nav class="abs nav">
    <span>Party Bus</span><i>|</i><span>Charter Bus</span><i>|</i><span>Party Trailer</span><i>|</i><span>Party Boat</span><i>|</i><span>House Bus</span><i>|</i><span>Want you own?</span>
  </nav>
</header>

<section class="abs hero" role="img" aria-label="Photo of guests partying inside a neon-lit party bus">
  <div class="abs hero-title">HOLLOWAY BUS</div>
  <div class="abs hero-sub">Ultimate Party Experience!</div>
  <div class="abs dots"><span></span><span></span><span></span></div>
</section>

<h2 class="abs welcome-title">Welcome to Holloway Bus Company</h2>
<p class="abs copy welcome-copy">Our staff of highly skilled drivers provide our passengers with professional service of unmatched luxury and quality. We take great pride in providing the very best in high quality affordable luxury transportation.This enables us to operate our party bus and limousine services with absolute confidence and pride. As a leading party bus and limo rental company we can provide you with a wide range of transportation services.</p>

<aside class="abs fb-box">
  <div class="row"><span class="mark"></span><span class="name">Holloway Bus</span></div>
  <div class="btn"></div>
  <hr>
  <div>9,890 people like <span class="name">Holloway Bus</span></div>
  <div class="faces"><span></span><span></span><span></span><span></span><span></span><span></span></div>
  <div class="foot">Social plugin</div>
</aside>

<h2 class="abs services-title">Our Services</h2>
<div class="abs gold-btn view-all">View All</div>

<article class="abs card" style="left:121px;top:533px">
  <div class="thumb" role="img" aria-label="Photo of a white stretch party bus" style="background:linear-gradient(#1a1a1a,#e8e8ee 60%,#3a3a3a)"></div>
  <h3>Party Bus</h3>
  <p>Lorem ipsum dolor sit amet, consectetur adipiscing elit. Curabitur venenatis <b>more..</b></p>
</article>
<article class="abs card" style="left:413px;top:533px">
  <div class="thumb" role="img" aria-label="Photo of a charter bus interior with patterned seats" style="background:linear-gradient(#d8d8d8,#3a5aa8 55%,#c03040)"></div>
  <h3>Charter Bus</h3>
  <p>Lorem ipsum dolor sit amet, consectetur adipiscing elit. Curabitur venenatis <b>more..</b></p>
</article>
<article class="abs card" style="left:121px;top:638px">
  <div class="thumb" role="img" aria-label="Photo of a party trailer lit up at night" style="background:linear-gradient(#0c1630,#3a3a8a 50%,#0a0a14)"></div>
  <h3>Party Trailer</h3>
  <p>Lorem ipsum dolor sit amet, consectetur adipiscing elit. Curabitur venenatis vehicula vitae <b>more..</b></p>
</article>
<article class="abs card" style="left:413px;top:638px">
  <div class="thumb" role="img" aria-label="Photo of a party boat on blue water" style="background:linear-gradient(#8cc0e8,#e8e8e8 45%,#2a90b0)"></div>
  <h3>Party Boat</h3>
  <p>Lorem ipsum dolor sit amet, consectetur adipiscing elit. Curabitur venenatis <b>more..</b></p>
</article>

<h2 class="abs coast-title">Best Way To See The Coast</h2>
<div class="abs coast-photo" role="img" aria-label="Photo of a cheering group on a boat at sea"></div>
<p class="abs copy coast-copy">Lorem ipsum dolor sit amet, consectetur adipiscing elit. Curabitur venenatis vehicula tellus, id mattis neque accumsan vitae. Fusce rhoncus erat in ullamcorper rutrum. Nam aliquam non neque eu rhoncus. Etiam euismod sed est quis porta. Aliquam erat volutpat. Aliquam erat volutpat. Donec lacinia, erat vel placerat tincidunt, erat libero pharetra erat, ac luctus enim tortor ac eros.</p>
<div class="abs gold-btn book">Book It Now</div>

<div class="abs rule" style="top:945px"></div>

<footer>
  <h2 class="abs foot-title" style="left:121px">Quotes &amp; Bookings</h2>
  <p class="abs copy quote-copy">Lorem ipsum dolor sit amet, consectetur adipiscing elit. Curabitur venenatis vehicula tellus, id mattis neque accumsan vitae. Fusce rhoncus erat in ullamcorper rutrum. Nam aliquam non neque eu rhoncus.</p>
  <div class="abs gold-btn get-quote">Get A Quote</div>

  <h2 class="abs foot-title" style="left:337px">Latest Blog Poste</h2>
  <div class="abs blog" style="top:990px">
    <div class="thumb" role="img" aria-label="Photo of party guests"></div>
    <h4>Lorem ipsum dolor sit amet</h4>
    <p>Consectetur adipiscing elit. Curabitur venenatis vehicula tellus, id</p>
  </div>
  <div class="abs blog" style="top:1051px">
    <div class="thumb" role="img" aria-label="Photo of party guests"></div>
    <h4>Lorem ipsum dolor sit amet</h4>
    <p>Consectetur adipiscing elit. Curabitur venenatis vehicula tellus, id</p>
  </div>

  <h2 class="abs foot-title" style="left:542px">Join Our VIP Club</h2>
  <p class="abs copy vip-copy">Lorem ipsum dolor sit amet, consectetur adipiscing elit.</p>
  <div class="abs field" style="top:1022px">Your Name</div>
  <div class="abs field" style="top:1049px">Email Address</div>
  <div class="abs gold-btn join">Join Now</div>

  <div class="abs rule" style="top:1114px"></div>
  <div class="abs copyright">Copyright 2014 Holloway Party company. All Rights Reserved.<br><a href="#">Privacy Policy</a></div>
  <div class="abs social foot-social"><span class="s1"></span><span class="s2"></span><span class="s3"></span></div>
</footer>
</body>
</html>
```